Meadowlark Counseling Partners, LLC Needs Modern Business Card Design.

We provide behavioral health services from western Kansas to eastern Kansas. There is an abundance of competition for the services we provide with our main competitor being larger and having significantly more financial resources; however, the quality of services we provide is greater and we have started to catch the attention of the State of Kansas. We had a great logo designed by ArtFolio - this will be used to build upon our brand. The logo (attached) should be used in the card development. We want something unique, modern, but also a card design that clearly states our name, contact info, provides the name and unqiue location of each clinician, etc. Rounded edges, or a unique size, just something that makes our business card stand out from others. I have also uploaded each clinician's name and their unique location and phone number.

Our idea is to have one side be black with our logo. Then, on the other side have business cards for each individual. Plus, we want one card that is "generic" with no specific clinician's name listed so that we can give clients an appointment card when they leave. Some clinicians have two locations - we're open to design and background color, but we have started going with branding colors of black, the yellow in the logo files attached, and sometimes a gray. Our new office has been decorated using this theme.

Target Market(s)

individuals and families in need of behavioral health services; potential professional referral sources; existing referral sources

Industry/Entity Type

Business

Contact Information for Business Card

I attached a Word doc that provides clinician names, credentials and location information specific to each individual.

Font styles to use
Serif

Colors
000000
fbed22
dbdbdb
9d9d9d
c3c3c3

Requirements
Must have
• 1) use of the company logo that has been attached; 2) a template that provides us space to individualize business cards for all of our clinicians; 3) should stick to the colors we are branding with: black, yellow from the logo file, maybe a gray shade and we're open to a suggestion on a shade of white.
Nice to have
• Group discussion culminated in the thought that one side would be black with just our logo - no clinician names, etc. A unique design - rounded edges, unique size, some catchy lay-out would be nice.
Should not have
• Must not be too busy. Should look "clean." The project should stick to branding colors: black, yellow (from the logo file), maybe a gray and shade of white.

```html
<!DOCTYPE html>
<html lang="en">
<head>
<meta charset="utf-8">
<title>Meadowlark Counseling Partners – Business Card</title>
<link rel="stylesheet" href="https://fonts.googleapis.com/css2?family=Lora:wght@400;600;700&display=swap">
<style>
  :root {
    --backdrop: #3a3b3d;
    --card: #1f2023;
    --yellow: #fbc21a;
    --white: #f2f2f2;
  }
  * { box-sizing: border-box; margin: 0; padding: 0; }
  html, body {
    width: 1200px; height: 1189px; overflow: hidden;
    background: var(--backdrop);
    font-family: "Lora", Georgia, serif;
  }
  .canvas { position: relative; width: 1200px; height: 1189px; }
  .card {
    position: absolute; left: 170px; width: 860px; height: 491px;
    background: var(--card);
    border-radius: 38px;
    box-shadow: 0 18px 40px rgba(0,0,0,.45);
    overflow: hidden;
  }
  .card--front { top: 70px; }
  .card--back { top: 628px; }

  .brand {
    position: absolute; text-align: center;
    color: var(--yellow); font-weight: 600; letter-spacing: .12em;
    text-transform: uppercase; line-height: 1.25;
  }
  .brand__dot {
    display: block; margin: 0 auto 18px;
    width: 70px; height: 70px; border-radius: 50%;
    background: var(--yellow);
  }
  .card--front .brand { left: 0; right: 0; top: 150px; }
  .card--front .brand__name { font-size: 52px; display: block; }
  .card--front .brand__sub { font-size: 21px; display: block; }

  .card--back .brand { right: 50px; top: 50px; width: 440px; }
  .card--back .brand__dot { width: 54px; height: 54px; margin-bottom: 14px; }
  .card--back .brand__name { font-size: 38px; display: block; }
  .card--back .brand__sub { font-size: 15px; display: block; }

  .person { position: absolute; left: 52px; top: 60px; }
  .person__name { color: var(--yellow); font-weight: 700; font-size: 30px; }
  .person__title { color: var(--white); font-size: 22px; margin-top: 2px; }

  .office { position: absolute; left: 92px; color: var(--white); font-size: 24px; line-height: 1.3; font-style: normal; }
  .office--one { top: 205px; }
  .office--two { top: 335px; }
  .office__phone { display: flex; align-items: center; gap: 12px; margin-top: 6px; }
  .phone-icon { width: 30px; height: 30px; flex: none; }

  .tagline {
    position: absolute; right: 50px; bottom: 55px;
    color: var(--white); font-size: 24px;
  }
</style>
</head>
<body>
<main class="canvas">
  <section class="card card--front" aria-label="Card front">
    <div class="brand">
      <span class="brand__dot"></span>
      <span class="brand__name">Meadowlark</span>
      <span class="brand__sub">Counseling Partners, LLC</span>
    </div>
  </section>

  <section class="card card--back" aria-label="Card back">
    <div class="person">
      <p class="person__name">Daniel R. Hollis, LP</p>
      <p class="person__title">President</p>
    </div>

    <address class="office office--one">
      418 N. Elm St.<br>Hays, Kansas 67601
      <span class="office__phone">
        <svg class="phone-icon" viewBox="0 0 30 30" aria-hidden="true">
          <circle cx="15" cy="15" r="13" fill="none" stroke="var(--yellow)" stroke-width="2.5"/>
          <path d="M8 12c0-2 3-3 7-3s7 1 7 3l-2 1.5-2-1v-1.2h-6V12.5l-2 1z M10 15h10v5H10z" fill="var(--yellow)"/>
        </svg>
        (785) 555-0142
      </span>
    </address>

    <address class="office office--two">
      207 E. Main St., Ste. 110<br>Salina, Kansas 67401
      <span class="office__phone">
        <svg class="phone-icon" viewBox="0 0 30 30" aria-hidden="true">
          <circle cx="15" cy="15" r="13" fill="none" stroke="var(--yellow)" stroke-width="2.5"/>
          <path d="M8 12c0-2 3-3 7-3s7 1 7 3l-2 1.5-2-1v-1.2h-6V12.5l-2 1z M10 15h10v5H10z" fill="var(--yellow)"/>
        </svg>
        (888) 555-0178
      </span>
    </address>

    <div class="brand">
      <span class="brand__dot"></span>
      <span class="brand__name">Meadowlark</span>
      <span class="brand__sub">Counseling Partners, LLC</span>
    </div>

    <p class="tagline">“Brighter days start here.”</p>
  </section>
</main>
</body>
</html>
```